London based Blowdry bar needs drinks menu

Volara Blowdry Bar is a successful trendy 'Blowdry bar' based in London. We offer our clients a number of services that are quick, affordable and ideal for a perfect night out!
Within the salon we offer soft & alcoholic drinks - I need to advertise this but space is limited. Therefore I would like to have a simple but pretty bar menu that will be designed like a banner and run under the mirrors at each position.
Please look at our website to have a look inside salon and pick up design ideas, colours used and feel of salon.
Website = www.quickstylelounge.co.uk
Font used for Volara logo = Houschka rounded
Font used on website = District Pro
Measurement for each menu 90cm length x 7.5cm height (horizontal menu)
Target Market(s)
20-50 year olds - clients in salon to have a fast fun experience. needs to be clear, easy to read and to the point
Font styles to use
Other font styles liked:
- District Pro
Requirements
Must have
- Title of drink, price of drink - easy to read font
Nice to have
- Nice to have a picture of drink in beginning of menu (nice visual add) to draw attention to clients eyes and so they understand it is a drinks menu. Clear points at the beginning of each drink.

```html
<!DOCTYPE html>
<html lang="en">
<head>
<meta charset="utf-8">
<title>Volara Blowdry Bar – Drinks Menu Banner</title>
<link rel="stylesheet" href="https://fonts.googleapis.com/css2?family=Oswald:wght@500;600;700&family=Baloo+2:wght@600;700&display=swap">
<style>
  :root {
    --page: #efefec;
    --banner: #ffffff;
    --green: #7cc24a;
    --ink: #222222;
    --pink-soft: #f6d6e0;
    --glass-dark: #2a2a2a;
  }
  * { box-sizing: border-box; margin: 0; padding: 0; }
  html, body {
    width: 1138px;
    height: 1200px;
    overflow: hidden;
    background: var(--page);
  }
  .canvas {
    position: relative;
    width: 1138px;
    height: 1200px;
  }
  .menu-banner {
    position: absolute;
    left: 19px;
    top: 554px;
    width: 1100px;
    height: 92px;
    background: var(--banner);
    box-shadow: 0 2px 8px rgba(0,0,0,0.12);
    display: flex;
    overflow: hidden;
  }
  .drink-visual {
    flex: 0 0 64px;
    height: 100%;
    background: linear-gradient(160deg, var(--pink-soft) 0%, #d9b7c2 45%, var(--glass-dark) 100%);
  }
  .menu-body {
    flex: 1;
    display: flex;
    flex-direction: column;
    padding: 4px 10px 6px 8px;
  }
  .menu-header {
    display: flex;
    align-items: baseline;
    justify-content: space-between;
    height: 32px;
  }
  .menu-title {
    font-family: "Oswald", sans-serif;
    font-weight: 700;
    font-size: 25px;
    color: var(--green);
    letter-spacing: 0.3px;
    margin-left: 150px;
  }
  .menu-slogan {
    font-family: "Baloo 2", sans-serif;
    font-weight: 700;
    font-style: italic;
    font-size: 18px;
    color: var(--green);
  }
  .drink-list {
    flex: 1;
    display: flex;
    align-items: center;
    justify-content: space-between;
    list-style: none;
  }
  .drink {
    display: flex;
    align-items: center;
    gap: 4px;
  }
  .drink-name {
    font-family: "Oswald", sans-serif;
    font-weight: 600;
    font-size: 12.5px;
    line-height: 1.15;
    color: var(--ink);
    text-align: right;
    white-space: nowrap;
  }
  .drink-note {
    display: block;
    font-weight: 500;
    font-size: 9.5px;
    line-height: 1.1;
  }
  .drink-name.left-align { text-align: left; }
  .price {
    flex: 0 0 42px;
    width: 42px;
    height: 42px;
    border-radius: 50%;
    border: 3px solid var(--green);
    background: var(--banner);
    display: flex;
    align-items: center;
    justify-content: center;
    font-family: "Oswald", sans-serif;
    font-weight: 700;
    font-size: 16px;
    color: var(--ink);
  }
  .price sup {
    font-size: 8px;
    vertical-align: top;
    position: relative;
    top: 2px;
  }
</style>
</head>
<body>
<div class="canvas">
  <section class="menu-banner" aria-label="Volara Blowdry Bar drinks menu">
    <div class="drink-visual" role="img" aria-label="Illustration of a sparkling drink in a glass with a pink splash"></div>
    <div class="menu-body">
      <header class="menu-header">
        <h1 class="menu-title">WHY NOT HAVE A DRINK?</h1>
        <p class="menu-slogan">Check out bar board for drink offers...</p>
      </header>
      <ul class="drink-list">
        <li class="drink"><span class="drink-name">Filtered<br>Water</span><span class="price">£0<sup>00</sup></span></li>
        <li class="drink"><span class="drink-name">Sparkling<br>Water</span><span class="price">£1<sup>50</sup></span></li>
        <li class="drink"><span class="drink-name">Fizzcola /<br>Diet Fizzcola</span><span class="price">£2<sup>00</sup></span></li>
        <li class="drink"><span class="drink-name">100% real<br>Fruit Juice</span><span class="price">£2<sup>00</sup></span></li>
        <li class="drink"><span class="drink-name">Dry<br>White Wine /<br>Red Wine</span><span class="price">£4<sup>00</sup></span></li>
        <li class="drink"><span class="drink-name">Prosecco /<br>Rose Prosecco</span><span class="price">£5<sup>00</sup></span></li>
        <li class="drink"><span class="drink-name left-align">Prosecco Cocktails<span class="drink-note">Choose from: Elderflower<br>Peach, Spritz &amp; Hibiscus</span></span><span class="price">£7<sup>00</sup></span></li>
      </ul>
    </div>
  </section>
</div>
</body>
</html>
```